KVB Business Card Design

We need a business card that emphasizes consulting services worldwide. The name of the company is KVB Consulting Group. We provide consulting services across several industries including but not limited to commodities, telecom, manufacturing, logistics, marketing and operations. We would like to see a creative design that emphasizes the global aspect, including Latin America and US markets, as well the bilingual nature of the service offerings.

The contact information section should include icons to represent the following data:
1) Name, Title and Company Name
2) Mobile Number
3) Skype ID
4) Email
5) Web Page
6) Location

We would like to see a card that emphasizes the worldwide concept. The back of the card should be simple, including only the logo (or a portion of the logo) and the slogan.

We would also like to see business cards in a booklet format. The colors to be used should be the same combination of colors used in the logos attached to this brief.

The logo design and some business card examples from Artvane Hub are attached for reference on style and look.

Target Market(s)

International business executives, 45-65 years of age, bilingual

Industry/Entity Type

Marketing

Colors
0792cd
34a7d8
85cae6
ffffff
cee9f5
ecf7fb

Requirements
Must have
• Please follow colors in logo attached.

2) Mobile Number
3) Skype ID
4) Email
5) Web Page
6) Location
Nice to have
• Global concept, consulting profile, diverse industry focus
Should not have
• No black color

```html
<!DOCTYPE html>
<html lang="en">
<head>
<meta charset="utf-8">
<title>KVB Consulting Group – Business Card</title>
<link rel="stylesheet" href="https://fonts.googleapis.com/css2?family=Cinzel:wght@400;600&family=Source+Sans+3:wght@400;600&display=swap">
<style>
  :root {
    --teal: #5cb9d1;
    --teal-light: #7ec8dc;
    --teal-frame: #93d1e2;
    --teal-text: #3fa7c8;
    --white: #ffffff;
    --grey-text: #6b6f73;
    --backdrop: #e4e6e8;
  }
  * { margin: 0; padding: 0; box-sizing: border-box; }
  html, body { width: 1200px; height: 900px; overflow: hidden; }
  body {
    background: var(--backdrop);
    display: flex;
    flex-direction: column;
    align-items: center;
    justify-content: center;
    gap: 50px;
  }
  .card {
    width: 640px;
    height: 370px;
    position: relative;
    overflow: hidden;
    box-shadow: 0 6px 18px rgba(60, 70, 80, 0.18);
  }

  /* ---------- front ---------- */
  .card-front { display: flex; }
  .front-identity {
    width: 42%;
    background: var(--teal);
    position: relative;
  }
  .holder {
    position: absolute;
    top: 34px;
    right: 22px;
    text-align: right;
    color: var(--white);
    z-index: 2;
  }
  .holder-name {
    font-family: "Cinzel", serif;
    font-size: 24px;
    font-weight: 400;
    letter-spacing: 0.5px;
    line-height: 1;
  }
  .holder-title {
    font-family: "Source Sans 3", sans-serif;
    font-size: 10px;
    letter-spacing: 2.5px;
    margin-top: 5px;
  }
  .emblem-frame {
    position: absolute;
    left: -40px;
    top: 122px;
    width: 250px;
    height: 260px;
    background: var(--teal-light);
    border: 2px solid var(--teal-frame);
    outline: 4px solid var(--teal-light);
    outline-offset: 6px;
  }
  .front-details {
    width: 58%;
    background: var(--white);
    padding: 42px 34px 0 40px;
  }
  .brand {
    display: flex;
    flex-direction: column;
    align-items: center;
  }
  .brand-mark {
    width: 36px;
    height: 36px;
    background: var(--teal);
    margin-bottom: 8px;
  }
  .brand-name {
    font-family: "Cinzel", serif;
    font-size: 22px;
    font-weight: 600;
    color: var(--grey-text);
    letter-spacing: 0.5px;
    line-height: 1;
  }
  .brand-slogan {
    font-family: "Source Sans 3", sans-serif;
    font-size: 9.5px;
    color: var(--teal-text);
    letter-spacing: 2.6px;
    margin-top: 4px;
  }
  .contacts {
    list-style: none;
    margin-top: 58px;
  }
  .contacts li {
    display: flex;
    align-items: center;
    gap: 10px;
    font-family: "Source Sans 3", sans-serif;
    font-size: 13px;
    font-weight: 600;
    color: var(--grey-text);
    height: 23px;
  }
  .contacts svg { width: 14px; height: 14px; flex: none; }

  /* ---------- back ---------- */
  .card-back { background: var(--teal); }
  .back-panel {
    position: absolute;
    left: 0; top: 0;
    width: 245px;
    height: 100%;
    background: var(--teal-light);
  }
  .back-panel .emblem-frame {
    left: -40px;
    top: 40px;
    width: 250px;
    height: 250px;
  }
  .fold-line {
    position: absolute;
    left: 245px;
    top: 0;
    height: 100%;
    width: 4px;
  }
  .back-brand {
    position: absolute;
    left: 290px;
    right: 30px;
    top: 130px;
    display: flex;
    flex-direction: column;
    align-items: center;
  }
  .back-brand .brand-mark {
    background: transparent;
    border: 2px solid var(--white);
  }
  .back-brand .brand-name { color: var(--white); font-size: 26px; }
  .back-brand .brand-slogan { color: var(--white); font-size: 11px; }
</style>
</head>
<body>

  <section class="card card-front" aria-label="Card front">
    <div class="front-identity">
      <div class="holder">
        <p class="holder-name">Marcus Aldane</p>
        <p class="holder-title">COMMUNITY MANAGER</p>
      </div>
      <div class="emblem-frame"></div>
    </div>
    <div class="front-details">
      <div class="brand">
        <div class="brand-mark"></div>
        <p class="brand-name">KVB Consulting Group</p>
        <p class="brand-slogan">CONSULTING SERVICES WORLDWIDE</p>
      </div>
      <ul class="contacts">
        <li>
          <svg viewBox="0 0 14 14" aria-hidden="true"><rect x="3.5" y="0.5" width="7" height="13" rx="1.5" fill="none" stroke="#5cb9d1" stroke-width="1.3"/><circle cx="7" cy="11" r="0.9" fill="#5cb9d1"/></svg>
          (03) 9000 4172
        </li>
        <li>
          <svg viewBox="0 0 14 14" aria-hidden="true"><circle cx="7" cy="7" r="6.5" fill="#5cb9d1"/></svg>
          kvbconsultinggroup
        </li>
        <li>
          <svg viewBox="0 0 14 14" aria-hidden="true"><rect x="0.5" y="2.5" width="13" height="9" fill="#5cb9d1"/><path d="M0.8 2.8 L7 8 L13.2 2.8" fill="none" stroke="#fff" stroke-width="1"/></svg>
          info@kvbconsultinggroup.com
        </li>
        <li>
          <svg viewBox="0 0 14 14" aria-hidden="true"><g fill="none" stroke="#5cb9d1" stroke-width="1.1"><circle cx="7" cy="7" r="6"/><ellipse cx="7" cy="7" rx="2.6" ry="6"/><line x1="1" y1="7" x2="13" y2="7"/></g></svg>
          www.kvbconsultinggroup.com
        </li>
        <li>
          <svg viewBox="0 0 14 14" aria-hidden="true"><path d="M7 1 L13.5 7 H11.5 V13 H8.5 V9 H5.5 V13 H2.5 V7 H0.5 Z" fill="#5cb9d1"/></svg>
          2/1180 Harbour Road, Elmvale 3190
        </li>
      </ul>
    </div>
  </section>

  <section class="card card-back" aria-label="Card back">
    <div class="back-panel">
      <div class="emblem-frame"></div>
    </div>
    <svg class="fold-line" viewBox="0 0 4 370" preserveAspectRatio="none" aria-hidden="true">
      <line x1="2" y1="0" x2="2" y2="370" stroke="#ffffff" stroke-width="3" stroke-dasharray="14 12"/>
    </svg>
    <div class="back-brand">
      <div class="brand-mark"></div>
      <p class="brand-name">KVB Consulting Group</p>
      <p class="brand-slogan">CONSULTING SERVICES WORLDWIDE</p>
    </div>
  </section>

</body>
</html>
```